I need a business Card Design for my practice , i am clinical herbalist. I am a herbalist specializing in Lyme disease, autism, autoimmune diseases, difficult to cure diseasesDifficult to cure diseases. In my innovative practice i link traditional medicine, herbs with science, immunologu ,pharmacology.

Industry/Entity Type

Business

Contact Information for Business Card

My company name : OSRODEK ZIELNIKA
My name : Piotr Weltak
Name of my profession : Fitoterapeuta
In Polish language Fitoterapeuta is Herbalist .

e-mail: piotrweltak@osrodekzielnika.com
www.osrodek-zielnika.pl
phone : 574 806 215
My company adress : Dąbrowa Sękowska 14 , 38-415 Mielnik
I dont have logo .

Requirements
Nice to have
• My company

```html
<!DOCTYPE html>
<html lang="pl">
<head>
<meta charset="utf-8">
<title>Ośrodek Zielnika – wizytówka</title>
<link rel="stylesheet" href="https://fonts.googleapis.com/css2?family=Alfa+Slab+One&family=Kanit:wght@500&family=Quicksand:wght@400;500&display=swap">
<style>
  :root {
    --page-bg: #ddd8d2;
    --card-top: #efece8;
    --card-bottom: #dcd8d3;
    --card-edge: rgba(255,255,255,0.85);
    --title-blue: #1d4f86;
    --name-blue: #173f6d;
    --role-ink: #2a2a2a;
    --accent-line: #1f5596;
    --panel-light: #2d64a0;
    --panel-dark: #103668;
    --contact-ink: #f4e6e6;
    --contact-soft: #e7b9b9;
    --icon-light: #f1eeee;
    --icon-rose: #e3a9a9;
    --icon-ink: #1d4f86;
  }
  * { box-sizing: border-box; margin: 0; padding: 0; }
  html, body {
    width: 1200px; height: 970px; overflow: hidden;
    background: var(--page-bg);
  }
  .business-card {
    position: absolute; left: 360px; top: 60px;
    width: 480px; height: 850px;
    border-radius: 16px;
    border: 1px solid var(--card-edge);
    background: linear-gradient(180deg, var(--card-top), var(--card-bottom));
    box-shadow: 0 14px 40px rgba(0,0,0,0.18);
    overflow: hidden;
  }
  .company-name {
    position: absolute; top: 72px; left: 0; width: 100%;
    text-align: center;
    font-family: "Alfa Slab One", serif;
    font-size: 74px; line-height: 1.1; letter-spacing: -1px;
    color: var(--title-blue);
    text-shadow: 0 2px 2px rgba(0,0,0,0.15);
    transform: scaleX(0.82);
  }
  .practitioner {
    position: absolute; right: 42px; top: 352px; text-align: right;
  }
  .practitioner-name {
    font-family: "Kanit", sans-serif; font-weight: 500;
    font-size: 31px; color: var(--name-blue); line-height: 1.1;
  }
  .practitioner-role {
    font-family: "Quicksand", sans-serif; font-weight: 500;
    font-size: 19px; color: var(--role-ink); margin-top: 6px;
  }
  .role-underline {
    width: 80px; height: 4px; background: var(--accent-line);
    margin: 10px 0 0 auto;
  }
  .contact-panel { position: absolute; left: 0; top: 0; }
  .contact-row {
    position: absolute; left: 74px;
    display: flex; align-items: center; gap: 14px;
    font-family: "Quicksand", sans-serif; font-size: 19px;
    color: var(--contact-ink); line-height: 1.3;
  }
  .contact-row.address { color: var(--contact-soft); }
  .contact-icon {
    width: 34px; height: 34px; border-radius: 5px; flex: none;
    display: flex; align-items: center; justify-content: center;
  }
  .contact-icon.light { background: var(--icon-light); }
  .contact-icon.rose { background: var(--icon-rose); }
</style>
</head>
<body>
  <main class="business-card">
    <h1 class="company-name">OSRODEK<br>ZIELNIKA</h1>

    <div class="practitioner">
      <p class="practitioner-name">Piotr Weltak</p>
      <p class="practitioner-role">Fitoterapeuta</p>
      <div class="role-underline"></div>
    </div>

    <svg class="contact-panel" width="480" height="850" aria-hidden="true">
      <defs>
        <linearGradient id="panelFill" x1="0" y1="0" x2="1" y2="1">
          <stop offset="0" stop-color="var(--panel-light)"/>
          <stop offset="1" stop-color="var(--panel-dark)"/>
        </linearGradient>
      </defs>
      <polygon points="80,457 449,477 409,760 26,760" fill="url(#panelFill)" opacity="0.93"/>
    </svg>

    <div class="contact-row phone" style="top:532px">
      <span class="contact-icon light">
        <svg width="20" height="20" viewBox="0 0 24 24"><path fill="var(--icon-ink)" d="M6.6 10.8a15.1 15.1 0 0 0 6.6 6.6l2.2-2.2a1 1 0 0 1 1-.25 11.4 11.4 0 0 0 3.6.57 1 1 0 0 1 1 1V20a1 1 0 0 1-1 1A17 17 0 0 1 3 4a1 1 0 0 1 1-1h3.5a1 1 0 0 1 1 1c0 1.25.2 2.45.57 3.57a1 1 0 0 1-.25 1z"/></svg>
      </span>
      <span>574 806 215</span>
    </div>

    <div class="contact-row web" style="top:610px">
      <span class="contact-icon rose">
        <svg width="20" height="20" viewBox="0 0 24 24" fill="none" stroke="var(--icon-ink)" stroke-width="2.4" stroke-linecap="round"><path d="M10 14a4 4 0 0 0 5.7 0l3-3a4 4 0 0 0-5.7-5.7l-1 1"/><path d="M14 10a4 4 0 0 0-5.7 0l-3 3a4 4 0 0 0 5.7 5.7l1-1"/></svg>
      </span>
      <span>piotrweltak@osrodekzielnika.com<br>www.osrodek-zielnika.pl</span>
    </div>

    <div class="contact-row address" style="top:672px">
      <span class="contact-icon rose">
        <svg width="20" height="20" viewBox="0 0 24 24"><path fill="var(--icon-ink)" d="M12 2a7 7 0 0 0-7 7c0 5 7 13 7 13s7-8 7-13a7 7 0 0 0-7-7zm0 9.5A2.5 2.5 0 1 1 12 6.5a2.5 2.5 0 0 1 0 5z"/></svg>
      </span>
      <span>Dąbrowa Sękowska 14 ,<br>38-415 Mielnik</span>
    </div>
  </main>
</body>
</html>
```